Redesign of existing business card

I would like the "signage" attachment converted into a business card. This needs to be double sided aswell, keeping the phone number and names on the front, and the email + website on the back.

Second attachment is the current business card design.

Larger font for contact details is required.

Must keep to original color themes (electric blue, silver/grey etc)

Back of the card to have blue background with white writing.

Industry/Entity Type

Business

Contact Information for Business Card

Refer to existing design from attachments

Requirements
Must have
• Refer to existing design from attachments
Nice to have

```html
<!DOCTYPE html>
<html lang="en">
<head>
<meta charset="utf-8">
<title>Volta Line Electrical – Business Card</title>
<link href="https://fonts.googleapis.com/css2?family=Exo+2:wght@500;600;700&display=swap" rel="stylesheet">
<style>
  :root {
    --electric-blue: #0000ff;
    --paper-white: #ffffff;
    --backdrop: #e6e7ea;
    --silver: #9a9da3;
  }
  * { margin: 0; padding: 0; box-sizing: border-box; }
  html, body {
    width: 1200px;
    height: 987px;
    overflow: hidden;
    background: var(--backdrop);
    font-family: "Exo 2", sans-serif;
  }
  .canvas {
    position: relative;
    width: 1200px;
    height: 987px;
  }
  .card {
    position: absolute;
    left: 293px;
    width: 615px;
    height: 352px;
    overflow: hidden;
  }
  .card--front { top: 130px; background: var(--paper-white); }
  .card--back { top: 506px; background: var(--electric-blue); }

  /* Front */
  .front-brand {
    position: absolute;
    left: 0; right: 0;
    top: 88px;
    display: flex;
    align-items: center;
    justify-content: center;
    gap: 14px;
  }
  .brand-dot {
    width: 66px; height: 66px;
    border-radius: 50%;
    background: var(--silver);
  }
  .brand-name {
    color: var(--electric-blue);
    font-weight: 700;
    font-size: 30px;
    line-height: 1;
    letter-spacing: 1px;
    text-transform: uppercase;
  }
  .contact-band {
    position: absolute;
    left: 0; right: 0;
    top: 244px;
    height: 76px;
    background: var(--electric-blue);
    color: var(--paper-white);
    display: flex;
    flex-direction: column;
    align-items: center;
    justify-content: center;
    gap: 6px;
  }
  .person { font-weight: 600; font-size: 22px; line-height: 1; }
  .person .role { font-size: 17px; font-weight: 500; }
  .phone {
    display: flex; align-items: center; gap: 6px;
    font-weight: 600; font-size: 20px; line-height: 1;
  }
  .phone svg { width: 24px; height: 24px; }

  /* Back */
  .back-brand {
    position: absolute;
    left: 110px;
    top: 118px;
    width: 140px;
    height: 116px;
    display: flex;
    flex-direction: column;
    align-items: center;
    justify-content: center;
    gap: 10px;
  }
  .back-brand .brand-dot { width: 60px; height: 60px; background: var(--paper-white); }
  .back-brand .brand-name { color: var(--paper-white); font-size: 20px; }
  .divider {
    position: absolute;
    left: 274px;
    top: 130px;
    width: 2px;
    height: 104px;
    background: var(--paper-white);
  }
  .web-details {
    position: absolute;
    left: 302px;
    top: 158px;
    color: var(--paper-white);
    font-weight: 500;
    font-size: 16px;
    line-height: 24px;
  }
</style>
</head>
<body>
<main class="canvas">
  <section class="card card--front" aria-label="Card front">
    <div class="front-brand">
      <span class="brand-dot"></span>
      <span class="brand-name">Volta Line Electrical</span>
    </div>
    <div class="contact-band">
      <p class="person">Daniel Reeve – <span class="role">CEO&amp;Founder</span></p>
      <p class="phone">
        <svg viewBox="0 0 24 24" aria-hidden="true">
          <circle cx="12" cy="12" r="10.5" fill="none" stroke="#fff" stroke-width="1.6"/>
          <path d="M8.2 6.5l1.9-.4 1.2 2.8-1.3 1c.6 1.4 1.7 2.6 3.1 3.3l1.1-1.3 2.8 1.2-.4 1.9c-.2.6-.7 1-1.4 1-4.4-.3-7.8-3.8-8.1-8.1 0-.7.4-1.2 1.1-1.4z" fill="#fff"/>
        </svg>
        0400 555 193
      </p>
    </div>
  </section>

  <section class="card card--back" aria-label="Card back">
    <div class="back-brand">
      <span class="brand-dot"></span>
      <span class="brand-name">Volta Line</span>
    </div>
    <span class="divider"></span>
    <div class="web-details">
      <p>dan@voltaline.com.au</p>
      <p>www.voltaline.com.au</p>
    </div>
  </section>
</main>
</body>
</html>
```